Letterhead

Create letterhead for corporate letters, proposals, thank yous, etc.

Target Market(s)

Technology, Communications

Industry/Entity Type

Information Technology

```html
<!DOCTYPE html>
<html lang="en">
<head>
<meta charset="utf-8">
<title>Tierline Letterhead Set</title>
<link rel="stylesheet" href="https://fonts.googleapis.com/css2?family=Questrial&display=swap">
<style>
  :root {
    --board: #ababab;
    --paper: #ffffff;
    --ink: #4a4a4a;
    --brand-blue: #1a8bc8;
    --soft-blue: #e3e9f2;
    --dark-sheet: #000000;
    --on-dark: #ffffff;
  }
  * { margin: 0; padding: 0; box-sizing: border-box; }
  html, body { width: 1200px; height: 2348px; overflow: hidden; }
  body {
    background: var(--board);
    font-family: "Questrial", "Century Gothic", sans-serif;
    position: relative;
  }
  .sheet {
    position: absolute;
    box-shadow: 0 4px 14px rgba(0,0,0,0.25);
    overflow: hidden;
  }
  .sheet--back { left: 328px; top: 152px; width: 800px; height: 1040px; background: var(--paper); }
  .sheet--front { left: 72px; top: 80px; width: 816px; height: 1032px; background: var(--paper); }
  .sheet--dark { left: 200px; top: 1232px; width: 800px; height: 1096px; background: var(--dark-sheet); }

  .brand-name {
    position: absolute;
    font-size: 42px;
    letter-spacing: 1px;
    color: var(--brand-blue);
    display: flex;
    align-items: center;
    gap: 14px;
    white-space: nowrap;
    line-height: 1;
  }
  .brand-dot { width: 16px; height: 16px; border-radius: 50%; background: currentColor; }
  .sheet--front .brand-name { left: 48px; top: 40px; }
  .sheet--back .brand-name { right: 40px; top: 44px; font-size: 36px; }
  .sheet--dark .brand-name { right: 56px; top: 80px; color: var(--on-dark); font-size: 48px; }

  .contact {
    position: absolute;
    font-size: 11px;
    font-style: normal;
    line-height: 16px;
    color: var(--ink);
    text-align: right;
  }
  .sheet--front .contact { right: 48px; top: 36px; }
  .sheet--back .contact { right: 40px; bottom: 20px; }
  .web-address { position: absolute; right: 40px; bottom: 24px; color: var(--on-dark); font-size: 15px; }

  .sweep { position: absolute; }
  .sheet--front .sweep {
    left: 40px; top: 520px; width: 776px; height: 512px;
    background: radial-gradient(ellipse at 90% 100%, var(--soft-blue) 0%, rgba(227,233,242,0.5) 40%, rgba(255,255,255,0) 72%);
  }
  .sheet--back .sweep {
    left: 540px; top: 620px; width: 260px; height: 360px;
    background: radial-gradient(ellipse at 80% 90%, var(--soft-blue) 0%, rgba(255,255,255,0) 70%);
  }
  .sheet--dark .sweep {
    left: 0; top: 560px; width: 800px; height: 536px;
    background: radial-gradient(ellipse at 30% 100%, var(--brand-blue) 0%, rgba(26,139,200,0.5) 40%, rgba(0,0,0,0) 72%);
  }
</style>
</head>
<body>
  <section class="sheet sheet--back" aria-label="Letterhead with footer contact">
    <div class="brand-name">Tierline<span class="brand-dot"></span></div>
    <div class="sweep" role="img" aria-label="Faint sweeping brand decoration"></div>
    <address class="contact">
      1420 Harbor Way, Oakdale, CA 90210<br>
      Tel 555 014 2290<br>
      hello@tierline-it.com
    </address>
  </section>

  <section class="sheet sheet--front" aria-label="Letterhead with header contact">
    <div class="brand-name">Tierline<span class="brand-dot"></span></div>
    <address class="contact">
      1420 Harbor Way<br>
      Oakdale, CA 90210<br>
      Tel 555 014 2290<br>
      hello@tierline-it.com
    </address>
    <div class="sweep" role="img" aria-label="Faint sweeping brand decoration"></div>
  </section>

  <section class="sheet sheet--dark" aria-label="Dark cover sheet">
    <div class="brand-name">Tierline<span class="brand-dot"></span></div>
    <div class="sweep" role="img" aria-label="Blue and grey sweeping brand decoration"></div>
    <div class="web-address">www.tierline-it.com</div>
  </section>
</body>
</html>
```